Banner Pop Up Opt In Form REDESIGNS - SLEEK BLACK LOOK

Please redesign banners attached.

I am looking for a very sleek look....I do not like this collage of images on these current designs. Please keep all content same but use images that pop.

I have an acccount at www.pixmorrow-example.com or you can use your own images.

I like black background for somereason because it looks very sleek....but these designs should pop , build trust and credibility and have easy opt in form....SLEEK AND MODERN LOOK is what im looking for....

Target Market(s)

Consumers on websites

Requirements
Must have
• Please redesign banners attached.

Nice to have

Should not have

```html
<!DOCTYPE html>
<html lang="en">
<head>
<meta charset="utf-8">
<title>Opt-in Banner Set – Sleek Black</title>
<link href="https://fonts.googleapis.com/css2?family=Bebas+Neue&family=Rajdhani:wght@600;700&family=Roboto:wght@400;500&display=swap" rel="stylesheet">
<style>
  :root{
    --page:#d7d7d7;
    --ink:#0d0f12;
    --panel:#15181c;
    --blue:#1f8fe9;
    --blue-deep:#1674c4;
    --yellow:#fcc50d;
    --white:#ffffff;
    --field-text:#6f6f6f;
  }
  *{box-sizing:border-box;margin:0;padding:0}
  html,body{width:1200px;height:520px;overflow:hidden;background:var(--page)}
  .board{position:relative;width:1200px;height:520px}
  .slot{position:absolute;width:193px;height:166px;overflow:hidden}
  .banner{
    position:absolute;left:0;top:0;width:414px;height:356px;
    transform:scale(.4658);transform-origin:0 0;
    background:linear-gradient(160deg,#23272d 0%,var(--ink) 55%,#050607 100%);
    overflow:hidden;
  }
  .banner__photo{
    position:absolute;inset:0;
    clip-path:polygon(0 100px,160px 100px,300px 356px,0 356px);
  }
  .banner__streak{
    position:absolute;inset:0;
    background:linear-gradient(115deg,transparent 52%,rgba(31,143,233,.28) 52%,rgba(31,143,233,.28) 60%,transparent 60%,transparent 70%,rgba(255,255,255,.06) 70%,rgba(255,255,255,.06) 78%,transparent 78%);
  }
  .badge{
    position:absolute;left:9px;top:5px;width:106px;height:106px;border-radius:50%;
    background:var(--yellow);display:flex;flex-direction:column;align-items:center;justify-content:center;
    font-family:'Bebas Neue',sans-serif;color:var(--ink);text-align:center;line-height:.92;font-size:17px;
    box-shadow:0 0 0 3px rgba(0,0,0,.35);
  }
  .badge .big{font-size:40px;line-height:.9}
  .badge .mid{font-size:23px;line-height:.9}
  .headline{
    position:absolute;left:122px;top:6px;width:290px;
    font-family:'Bebas Neue',sans-serif;color:var(--blue);font-size:62px;line-height:51px;letter-spacing:1px;
  }
  .headline--win{top:10px}
  .subhead{
    position:absolute;left:134px;top:119px;width:270px;
    font-family:'Rajdhani',sans-serif;font-weight:600;color:var(--white);font-size:16.5px;line-height:17px;letter-spacing:.3px;
  }
  .form{position:absolute;left:163px;top:172px;width:212px}
  .field{
    height:28px;margin-bottom:8px;background:var(--white);border-radius:3px;
    font-family:'Roboto',sans-serif;font-size:12px;color:var(--field-text);padding:7px 8px 0;
  }
  .submit{
    height:28px;border-radius:3px;background:var(--blue);color:var(--white);
    font-family:'Rajdhani',sans-serif;font-weight:700;font-size:15px;text-align:center;line-height:28px;
  }
  .footer{
    position:absolute;left:0;right:0;bottom:0;height:34px;background:rgba(0,0,0,.85);
  }
  .footer p{
    position:absolute;left:162px;top:6px;font-family:'Roboto',sans-serif;font-weight:500;
    font-size:8.3px;line-height:10.5px;color:var(--white);
  }
  .photo-vegas{background:linear-gradient(180deg,#7d8fc4 0%,#c78a68 45%,#5a3d48 75%,#2a2433 100%)}
  .photo-beach{background:linear-gradient(180deg,#9cc8ec 0%,#d9eef8 38%,#5fc0d3 50%,#e8cfa3 62%,#c59865 100%)}
  .photo-travel{background:linear-gradient(180deg,#c9c6c2 0%,#e9e7e3 40%,#8c8a88 70%,#3d3d3d 100%)}
  .photo-watch{background:linear-gradient(160deg,#9aa0a8 0%,#c7b3a3 35%,#9b7460 60%,#3f454c 100%)}
  .photo-dining{background:linear-gradient(180deg,#4a3526 0%,#b07a3e 30%,#6b3a2e 60%,#3a1c1f 100%)}
</style>
</head>
<body>
<main class="board">

  <!-- Row 1: offer banners -->
  <div class="slot" style="left:62px;top:89px"><section class="banner">
    <div class="banner__photo photo-vegas" role="img" aria-label="Las Vegas strip skyline at dusk"></div>
    <div class="banner__streak"></div>
    <div class="badge"><span>1-4 Night</span><span>Las Vegas</span><span>Hotel &amp; Casino</span></div>
    <h2 class="headline">Want a great<br>offer?</h2>
    <p class="subhead">SUBSCRIBE TO OUR NEWSLETTER<br>AND RECEIVE A COMPLIMENTARY</p>
    <div class="form"><div class="field">Name</div><div class="field">Email</div><div class="field">Phone</div><div class="submit">SUBMIT</div></div>
    <div class="footer"><p>We will send an email and a text message with<br>the offer and instructions on how to redeem.</p></div>
  </section></div>

  <div class="slot" style="left:282px;top:89px"><section class="banner">
    <div class="banner__photo photo-beach" role="img" aria-label="Tropical beach with lounge chair"></div>
    <div class="banner__streak"></div>
    <div class="badge"><span>7 Night</span><span>Resort/Condo</span><span>3,500+</span><span>Locations</span></div>
    <h2 class="headline">Want a great<br>offer?</h2>
    <p class="subhead">SUBSCRIBE TO OUR EMAIL LIST<br>AND RECEIVE A COMPLIMENTARY</p>
    <div class="form"><div class="field">Name</div><div class="field">Email</div><div class="field">Phone</div><div class="submit">SUBMIT</div></div>
    <div class="footer"><p>We will send an email and a text message with<br>the offer and instructions on how to redeem.</p></div>
  </section></div>

  <div class="slot" style="left:502px;top:89px"><section class="banner">
    <div class="banner__photo photo-travel" role="img" aria-label="Traveler with yellow suitcase in hotel lobby"></div>
    <div class="banner__streak"></div>
    <div class="badge"><span class="big">$500</span><span>Hotel Savings</span><span>Card</span></div>
    <h2 class="headline">Want a great<br>offer?</h2>
    <p class="subhead">SUBSCRIBE TO OUR EMAIL LIST<br>AND RECEIVE A COMPLIMENTARY</p>
    <div class="form"><div class="field">Name</div><div class="field">Email</div><div class="field">Phone</div><div class="submit">SUBMIT</div></div>
    <div class="footer"><p>We will send an email and a text message with<br>the offer and instructions on how to redeem.</p></div>
  </section></div>

  <div class="slot" style="left:721px;top:89px"><section class="banner">
    <div class="banner__photo photo-watch" role="img" aria-label="Wrist wearing a smart fitness watch"></div>
    <div class="banner__streak"></div>
    <div class="badge"><span class="mid">Smart</span><span class="mid">Fitness</span><span class="mid">Watch</span></div>
    <h2 class="headline">Want a great<br>offer?</h2>
    <p class="subhead">SUBSCRIBE TO OUR NEWSLETTER<br>AND RECEIVE A COMPLIMENTARY</p>
    <div class="form"><div class="field">Name</div><div class="field">Email</div><div class="field">Phone</div><div class="submit">SUBMIT</div></div>
    <div class="footer"><p>We will send an email and a text message with<br>the offer and instructions on how to redeem.</p></div>
  </section></div>

  <div class="slot" style="left:941px;top:89px"><section class="banner">
    <div class="banner__photo photo-dining" role="img" aria-label="Warmly lit restaurant dining room"></div>
    <div class="banner__streak"></div>
    <div class="badge"><span class="mid">$300</span><span class="mid">Restaurant</span><span class="mid">Certificate</span></div>
    <h2 class="headline">Want a great<br>offer?</h2>
    <p class="subhead">SUBSCRIBE TO OUR NEWSLETTER<br>AND RECEIVE A COMPLIMENTARY</p>
    <div class="form"><div class="field">Name</div><div class="field">Email</div><div class="field">Phone</div><div class="submit">SUBMIT</div></div>
    <div class="footer"><p>We will send an email and a text message with<br>the offer and instructions on how to redeem.</p></div>
  </section></div>

  <!-- Row 2: giveaway banners -->
  <div class="slot" style="left:62px;top:266px"><section class="banner">
    <div class="banner__photo photo-vegas" role="img" aria-label="Las Vegas strip skyline at dusk"></div>
    <div class="banner__streak"></div>
    <div class="badge"><span>1-4 Night</span><span>Las Vegas</span><span>Hotel &amp; Casino</span></div>
    <h2 class="headline headline--win">Enter to win</h2>
    <p class="subhead" style="top:76px">SUBSCRIBE TO OUR NEWSLETTER<br>TO ENTER TO WIN A</p>
    <div class="form" style="top:137px"><div class="field">Name</div><div class="field">Email</div><div class="field">Phone</div><div class="submit">SUBMIT</div></div>
    <div class="footer"><p>We will send an email and a text message with<br>the offer and instructions on how to redeem.</p></div>
  </section></div>

  <div class="slot" style="left:282px;top:266px"><section class="banner">
    <div class="banner__photo photo-beach" role="img" aria-label="Tropical beach with lounge chair"></div>
    <div class="banner__streak"></div>
    <div class="badge"><span>7 Night</span><span>Resort/Condo</span><span>3,500+</span><span>Locations</span></div>
    <h2 class="headline headline--win">Enter to win</h2>
    <p class="subhead" style="top:70px">SUBSCRIBE TO OUR EMAIL LIST<br>TO ENTER TO WIN A</p>
    <div class="form" style="top:130px"><div class="field">Name</div><div class="field">Email</div><div class="field">Phone</div><div class="submit">SUBMIT</div></div>
    <div class="footer"><p>We will send an email and a text message with<br>the offer and instructions on how to redeem.</p></div>
  </section></div>

  <div class="slot" style="left:502px;top:266px"><section class="banner">
    <div class="banner__photo photo-travel" role="img" aria-label="Traveler with yellow suitcase in hotel lobby"></div>
    <div class="banner__streak"></div>
    <div class="badge"><span class="big">$500</span><span>Hotel Savings</span><span>Cards</span></div>
    <h2 class="headline headline--win" style="top:20px">Enter to win</h2>
    <p class="subhead" style="top:89px">SUBSCRIBE TO OUR EMAIL LIST<br>AND RECEIVE A COMPLIMENTARY</p>
    <div class="form" style="top:144px"><div class="field">Name</div><div class="field">Email</div><div class="field">Phone</div><div class="submit">SUBMIT</div></div>
    <div class="footer"><p>We will send an email and a text message with<br>the offer and instructions on how to redeem.</p></div>
  </section></div>

  <div class="slot" style="left:721px;top:266px"><section class="banner">
    <div class="banner__photo photo-watch" role="img" aria-label="Wrist wearing a smart fitness watch"></div>
    <div class="banner__streak"></div>
    <div class="badge"><span class="mid">Smart</span><span class="mid">Fitness</span><span class="mid">Watch</span></div>
    <h2 class="headline headline--win">Enter to win</h2>
    <p class="subhead" style="top:72px">SUBSCRIBE TO OUR NEWSLETTER<br>TO ENTER TO WIN A</p>
    <div class="form" style="top:135px"><div class="field">Name</div><div class="field">Email</div><div class="field">Phone</div><div class="submit">SUBMIT</div></div>
    <div class="footer"><p>We will send an email and a text message with<br>the offer and instructions on how to redeem.</p></div>
  </section></div>

  <div class="slot" style="left:941px;top:266px"><section class="banner">
    <div class="banner__photo photo-dining" role="img" aria-label="Warmly lit restaurant dining room"></div>
    <div class="banner__streak"></div>
    <div class="badge"><span class="mid">$300</span><span class="mid">Restaurant</span><span class="mid">Certificate</span></div>
    <h2 class="headline headline--win" style="top:4px">Enter to win</h2>
    <p class="subhead" style="top:70px">SUBSCRIBE TO OUR NEWSLETTER<br>TO&nbsp; ENTER TO WIN A</p>
    <div class="form" style="top:125px"><div class="field">Name</div><div class="field">Email</div><div class="field">Phone</div><div class="submit">SUBMIT</div></div>
    <div class="footer"><p>We will send an email and a text message with<br>the offer and instructions on how to redeem.</p></div>
  </section></div>

</main>
</body>
</html>
```